Business card website / business card for website

We are a French website selling products Made in USA of quality, we need a business card to give from hand to hand and for deposit in the cartons of Each order. We-have the logo That I send in the attachments The theme is: US Vintage and find the compromised entre les national park ambience us and the atmosphere Brooklyn If you can make the feeling it's great The site www.lecomptoirdubisonroux.com (opening April) You can change the logo a little gold in color it could ... we are a French website selling products Made in USA quality, we need a business card to give from hand to hand and deposit in cartons each order. we have the logo that I convey in the attached parts is the theme: Vintage embiance US and find a compromise between the atmosphere us national park and the atmosphere Brooklyn at: www.lecomptoirdubisonroux.com (opening April) if you can the impression is great

Target Market(s)

25-50 YEARS man, woman.

Industry/Entity Type

Business

Contact Information for Business Card

www.lecomptoirdubisonroux.com
N'oubliez pas que nous sommes là si vous avez besoin de nouscontact@lecomptoirdubisonroux.com

Font styles to use
Serif

Requirements
Must have
• my logo with "general store", my email address preceded by the phrase: Do not forget that we are here if you need us My logo with the words "general store," my email address Preceded by the sentence: remember we're here if you need us (in french)
Nice to have
• i like this style: http://designpalettehub.com/inspiration/print-inspiration/25-beautiful-vintage-style-business-card-designs/ must feel the Vintage America it must feel the Vintage America lice can change a little logo or to color ... You can change the logo a little gold in color it could ... i like kraft paper with red ....
Should not have

```html
<!DOCTYPE html>
<html lang="fr">
<head>
<meta charset="utf-8">
<title>Le Comptoir du Bison Roux — Carte de visite</title>
<link rel="stylesheet" href="https://fonts.googleapis.com/css2?family=Open+Sans:wght@400;600&display=swap">
<style>
  :root {
    --backdrop: #3a3b3e;
    --card-white: #ffffff;
    --card-black: #1c1c1d;
    --band: #1a1a1a;
    --ink: #111111;
    --paper-line: #d9d9d9;
    --pattern-top: #2a2a2b;
    --pattern-bottom: #151516;
  }
  * { box-sizing: border-box; margin: 0; padding: 0; }
  html, body {
    width: 1200px; height: 864px; overflow: hidden;
    background: var(--backdrop);
    font-family: "Open Sans", Arial, sans-serif;
  }
  .sheet {
    position: relative; width: 1200px; height: 864px;
    display: flex; flex-direction: column; align-items: center; justify-content: center; gap: 48px;
  }
  .card {
    position: relative; width: 630px; height: 360px; overflow: hidden;
    border-radius: 3px;
    box-shadow: 0 10px 28px rgba(0,0,0,.35);
  }

  /* Back of the card */
  .card--back { background: var(--card-black); }
  .card--back .barn-pattern {
    position: absolute; inset: 0;
    background: linear-gradient(160deg, var(--pattern-top), var(--pattern-bottom));
  }
  .card--back .brand {
    position: absolute; left: 50%; top: 50%; transform: translate(-50%, -50%);
    display: flex; align-items: center; gap: 14px;
    color: var(--card-white); font-weight: 600; font-size: 22px; letter-spacing: .5px;
    white-space: nowrap;
  }
  .brand__dot {
    width: 30px; height: 30px; border-radius: 50%;
    border: 2px solid currentColor;
  }

  /* Front of the card */
  .card--front { background: var(--card-white); }
  .card--front .band {
    position: absolute; left: 0; right: 0; top: 78px; height: 96px;
    background: var(--band);
  }
  .card--front .brand {
    position: absolute; left: 24px; top: 38px;
    width: 124px; height: 124px; border-radius: 50%;
    background: var(--card-white); border: 2px solid var(--paper-line);
    display: flex; align-items: center; justify-content: center;
    padding: 14px; text-align: center;
    color: var(--ink); font-weight: 600; font-size: 14px; line-height: 1.3;
  }
  .card--front .store-label {
    position: absolute; right: 26px; top: 106px;
    color: var(--card-white); font-weight: 600; font-size: 30px; letter-spacing: .2px;
  }
  .contact {
    position: absolute; right: 26px; top: 200px;
    list-style: none; text-align: right;
    color: var(--ink); font-size: 15px; line-height: 1;
  }
  .contact li { margin-bottom: 22px; display: flex; justify-content: flex-end; align-items: center; gap: 8px; }
  .contact .icon { width: 14px; height: 14px; flex: none; }
</style>
</head>
<body>
<main class="sheet">

  <section class="card card--back" aria-label="Verso de la carte">
    <div class="barn-pattern" role="img" aria-label="Gravure ton sur ton d'une grange en bois entourée de sapins"></div>
    <div class="brand">
      <span class="brand__dot"></span>
      <span class="brand__title">Le Comptoir du Bison Roux</span>
    </div>
  </section>

  <section class="card card--front" aria-label="Recto de la carte">
    <div class="band"></div>
    <div class="brand">Le Comptoir du Bison Roux</div>
    <h1 class="store-label">General Store</h1>
    <ul class="contact">
      <li>N'oubliez pas que nous sommes là si vous avez besoin de</li>
      <li>nouscontact@lecomptoirdubisonroux.com
        <svg class="icon" viewBox="0 0 14 14" aria-hidden="true"><rect x="1" y="3" width="12" height="8" fill="#222"/><path d="M1 3 L7 8 L13 3" fill="none" stroke="#fff" stroke-width="1"/></svg>
      </li>
      <li>www.lecomptoirdubisonroux.com
        <svg class="icon" viewBox="0 0 14 14" aria-hidden="true"><circle cx="7" cy="7" r="6" fill="#222"/><path d="M1 7 H13 M7 1 C4 4 4 10 7 13 M7 1 C10 4 10 10 7 13" fill="none" stroke="#fff" stroke-width=".8"/></svg>
      </li>
    </ul>
  </section>

</main>
</body>
</html>
```